We are in search of a new business card design for our business. We have a Mexican Grocery Store called Tortilla Grove Market, we would like to see that some have mexican design, but we are open to any type of designs.

Phone: to be announced
Fax: to be announced

Address is:
2415 Calloway Blvd
Fairhaven, MD 21290

```html
<!DOCTYPE html>
<html lang="en">
<head>
<meta charset="utf-8">
<title>Tortilla Grove Market – Business Card</title>
<link href="https://fonts.googleapis.com/css2?family=Montserrat:wght@300;400;600;800&display=swap" rel="stylesheet">
<style>
  :root{
    --stage:#e6e7e8;
    --card:#ffffff;
    --ink:#1c1d1f;
    --red:#d1232a;
    --yellow:#fcc012;
    --ghost:#f3f3f3;
    --text:#222222;
  }
  *{box-sizing:border-box;margin:0;padding:0}
  html,body{width:1200px;height:927px;overflow:hidden;background:var(--stage)}
  body{position:relative;font-family:"Montserrat",sans-serif;color:var(--text)}
  .card{
    position:absolute;left:376px;top:72px;width:448px;height:782px;
    background:var(--card);border-radius:32px;overflow:hidden;
  }
  .card__header{position:absolute;left:0;top:0;width:448px;height:150px}
  .brand{
    position:absolute;left:0;right:0;top:190px;
    display:flex;flex-direction:column;align-items:center;gap:12px;
  }
  .brand__dot{width:24px;height:24px;border-radius:50%;background:var(--red)}
  .brand__name{
    font-weight:800;font-size:34px;line-height:1.1;color:var(--red);
    text-align:center;letter-spacing:.5px;
  }
  .brand-ghost{
    position:absolute;left:54px;top:470px;width:340px;height:340px;
    border-radius:50%;background:var(--ghost);
  }
  .person{position:absolute;left:0;right:0;top:412px;text-align:center}
  .person__name{font-weight:600;font-size:25px;color:var(--red);letter-spacing:.5px;line-height:30px}
  .person__role{font-weight:300;font-size:19px;line-height:24px;color:var(--text)}
  .contact{position:absolute;left:0;right:0;top:562px;text-align:center;font-weight:300;font-size:19px;line-height:24px}
  .contact__icons{display:flex;justify-content:center;gap:8px;margin:8px 0 8px}
  .contact__icons svg{width:13px;height:13px;fill:var(--red)}
  .card__footer{position:absolute;left:0;bottom:0;width:448px;height:34px}
  .footer__block{position:absolute;top:0;height:34px}
  .footer__block--left{left:0;width:80px;background:var(--yellow)}
  .footer__block--mid{left:87px;width:275px;background:var(--ink)}
  .footer__block--right{left:370px;width:78px;background:var(--yellow)}
</style>
</head>
<body>
  <div class="card">
    <svg class="card__header" viewBox="0 0 448 150" aria-hidden="true">
      <path fill="var(--red)" d="M0,0 H226 C196,8 178,32 160,66 C140,104 104,124 0,144 Z"/>
      <path fill="var(--red)" d="M448,0 H222 C252,8 270,32 288,66 C308,104 344,124 448,144 Z"/>
      <path fill="var(--ink)" d="M0,0 H222 C192,4 172,26 154,60 C134,96 100,114 0,136 Z"/>
      <path fill="var(--ink)" d="M448,0 H226 C256,4 276,26 294,60 C314,96 348,114 448,136 Z"/>
    </svg>

    <span class="brand-ghost" aria-hidden="true"></span>

    <div class="brand">
      <span class="brand__dot"></span>
      <p class="brand__name">Tortilla Grove<br>Market</p>
    </div>

    <div class="person">
      <p class="person__name">MARCUS BENNETT</p>
      <p class="person__role">Owner</p>
    </div>

    <div class="contact">
      <p>2415 Calloway Blvd</p>
      <p>Fairhaven, MD 21290</p>
      <div class="contact__icons">
        <svg viewBox="0 0 24 24" aria-label="Phone"><path d="M6.6 10.8a15 15 0 0 0 6.6 6.6l2.2-2.2c.3-.3.7-.4 1-.2 1.1.4 2.3.6 3.6.6.6 0 1 .4 1 1V20c0 .6-.4 1-1 1A17 17 0 0 1 3 4c0-.6.4-1 1-1h3.5c.6 0 1 .4 1 1 0 1.3.2 2.5.6 3.6.1.3 0 .7-.2 1z"/></svg>
        <svg viewBox="0 0 24 24" aria-label="Fax"><path d="M6 2h12v5H6zM4 8h16a2 2 0 0 1 2 2v7h-4v5H6v-5H2v-7a2 2 0 0 1 2-2zm4 8v4h8v-4z"/></svg>
      </div>
      <p>410.555.0148</p>
      <p>410.555.0163</p>
    </div>

    <div class="card__footer">
      <span class="footer__block footer__block--left"></span>
      <span class="footer__block footer__block--mid"></span>
      <span class="footer__block footer__block--right"></span>
    </div>
  </div>
</body>
</html>
```